Web Design Lumora Lane is a market place for handcrafts products

design a landing home page , and a product page ,
for a market place CMS that will sell handcrafts ..

Target Market(s)

Market place for Handicrafts makers

Number of Pages Required

2 page

Requirements
Nice to have
• Search Google images for Marrakech Old Medina , and Istanbul Copper Arcade

```html
<!DOCTYPE html>
<html lang="en">
<head>
<meta charset="utf-8">
<title>Lumora Lane — Handmade Marketplace</title>
<link href="https://fonts.googleapis.com/css2?family=Poppins:wght@400;500;600;700&family=Raleway:wght@500;600&display=swap" rel="stylesheet">
<style>
:root{
  --black:#000;
  --ink:#222;
  --text:#333;
  --muted:#555;
  --hero-bg:#f2f2f2;
  --strip-bg:#f4f4f4;
  --red:#e53935;
  --footer:#3d3d3d;
  --footer-base:#343434;
  --white:#fff;
  --link:#2a55c9;
}
*{margin:0;padding:0;box-sizing:border-box}
html,body{width:1200px;height:2831px;overflow:hidden;background:var(--white)}
body{position:relative;font-family:"Poppins",sans-serif;color:var(--text)}
.abs{position:absolute}

/* top bar and nav */
.announce{left:0;top:0;width:1200px;height:40px;background:var(--black);color:var(--white);font-size:11px;font-weight:500;display:flex;align-items:center;justify-content:center}
.nav{left:0;top:40px;width:1200px;height:38px;background:var(--black);border-top:1px solid #222}
.brand{left:244px;top:0;width:105px;height:38px;background:#111;display:flex;flex-direction:column;align-items:center;justify-content:center;color:var(--white);font-size:10px;font-weight:500;gap:2px}
.brand-dot{width:12px;height:12px;border-radius:50%;background:#c8502a}
.menu{left:415px;top:0;height:38px;display:flex;align-items:center;gap:10px;color:var(--white);font-size:9.5px;font-weight:500}
.menu .home{margin-right:8px}
.menu span.dd::after{content:" ▾";font-size:9px}
.icons{left:855px;top:9px;display:flex;gap:12px}
.icons svg{width:16px;height:16px}

/* hero */
.hero{left:0;top:81px;width:1200px;height:404px;background:var(--hero-bg)}
.hero-photo{left:254px;top:20px;width:278px;height:367px;background:linear-gradient(160deg,#f4efe6 0%,#e6d6c0 45%,#b9865c 60%,#efe7dc 75%,#8b7a64 100%);box-shadow:2px 3px 6px rgba(0,0,0,.2)}
.hero-title{left:553px;top:120px;width:400px;text-align:center;font-family:"Raleway",sans-serif;font-weight:600;font-size:35px;color:var(--ink)}
.hero-sub{left:553px;top:170px;width:400px;text-align:center;font-family:"Raleway",sans-serif;font-weight:600;font-size:18px;color:var(--ink);letter-spacing:.3px}
.btn-dark{left:665px;top:223px;width:152px;height:34px;border-radius:17px;background:#2b2b2b;color:var(--white);font-size:13px;font-weight:600;display:flex;align-items:center;justify-content:center;box-shadow:6px 4px 0 #b5b5b5}
.arrow{width:30px;height:46px}
.dots{left:601px;top:378px;display:flex;gap:7px}
.dots i{width:11px;height:11px;border-radius:50%;background:var(--red);display:block}
.dots i.on{background:#555}

/* section titles */
.section-title{left:0;width:1200px;text-align:center;font-size:20px;font-weight:400;color:var(--ink)}
.rule{height:2px;background:var(--ink)}

/* products */
.card{width:170px}
.card-photo{width:170px;height:205px;position:relative;box-shadow:2px 3px 5px rgba(0,0,0,.25)}
.badge{position:absolute;left:0;top:13px;width:46px;height:16px;background:var(--red);color:var(--white);font-size:9px;font-weight:600;display:flex;align-items:center;justify-content:center}
.card-name{margin-top:14px;text-align:center;font-size:9px;color:var(--muted)}
.card-price{text-align:center;font-size:9px;font-weight:600;color:var(--ink)}
.ph-clay{background:linear-gradient(135deg,#c49a80 0%,#7f6d5b 45%,#9a8a78 100%)}
.ph-beads{background:linear-gradient(150deg,#3f5f8a 0%,#1630a8 45%,#0b1a70 80%,#6f8aa8 100%)}
.ph-pipe{background:linear-gradient(160deg,#4a3a26 0%,#9f7a3c 40%,#e8e0d0 55%,#3b2e22 100%)}
.ph-lantern{background:radial-gradient(circle at 55% 45%,#b79a2a 0%,#4a5a2a 35%,#1b160f 75%)}

/* collections */
.tile{display:flex;align-items:center;justify-content:center;text-align:center;color:var(--white);font-weight:600;text-transform:none;box-shadow:2px 3px 6px rgba(0,0,0,.3)}
.tile.big{font-size:25px;font-weight:700;line-height:1.2}
.tile.small{font-size:15px;line-height:1.5}
.t-ceramic{background:linear-gradient(180deg,#8a7460 0%,#7a5a3c 40%,#5a4634 100%)}
.t-embroid{background:linear-gradient(150deg,#5e1f1f 0%,#7e2a2c 45%,#3e2a2a 100%)}
.t-treasure{background:linear-gradient(160deg,#6a5a3a 0%,#8a6a2a 45%,#3a2c1c 100%)}
.t-unique{background:radial-gradient(circle at 50% 60%,#3d5660 0%,#12181b 45%,#050505 100%)}
.t-handy{background:linear-gradient(140deg,#6a3a34 0%,#5a5870 45%,#8a6040 100%)}

/* offers strip */
.strip{left:4px;top:1973px;width:1196px;height:256px;background:var(--strip-bg)}
.strip-head{left:256px;top:1985px;font-size:13px;color:var(--ink)}
.strip-head .hl{color:var(--red)}
.strip-head a{color:var(--link);font-size:10px;margin-left:8px;text-decoration:underline}
.offer{width:127px;height:189px;box-shadow:2px 3px 5px rgba(0,0,0,.2)}
.o1{background:linear-gradient(180deg,#e9dccb 0%,#b7865a 60%,#8a5a32 100%)}
.o2{background:linear-gradient(170deg,#3e3a34 0%,#2e4e5e 50%,#6a4a32 100%)}
.o3{background:linear-gradient(180deg,#f0e9dc 0%,#e3d7c5 100%)}
.o4{background:linear-gradient(170deg,#3a2c22 0%,#8a5c34 55%,#2a1e16 100%)}
.o5{background:linear-gradient(180deg,#e9dcc7 0%,#d8c3a3 100%)}

/* promos */
.promo{width:340px;height:203px;color:var(--white);text-align:center;box-shadow:2px 3px 6px rgba(0,0,0,.3)}
.promo-lantern{background:radial-gradient(circle at 40% 55%,#3a5a8a 0%,#2a2430 50%,#1a1410 100%)}
.promo-copper{background:radial-gradient(circle at 50% 55%,#6a5038 0%,#3a2c22 55%,#1e1812 100%)}
.promo-text{position:absolute;left:0;top:78px;width:100%;font-size:17px;font-weight:700;line-height:17px}
.btn-white{position:absolute;left:111px;top:140px;width:119px;height:29px;border-radius:15px;background:var(--white);color:var(--ink);font-size:12px;font-weight:600;display:flex;align-items:center;justify-content:center}

/* footer */
.footer{left:0;top:2502px;width:1200px;height:260px;background:var(--footer);color:var(--white)}
.footer-base{left:0;top:2762px;width:1200px;height:69px;background:var(--footer-base);color:var(--white);font-size:9px;display:flex;align-items:center;justify-content:center}
.f-col h4{font-size:10px;font-weight:600;margin-bottom:14px}
.f-col p{font-size:8.5px;line-height:19px}
.f-contact p{line-height:23px}
.follow{left:303px;top:172px;font-size:10px;font-weight:600}
.social{left:305px;top:196px;display:flex;gap:8px}
.social span{width:25px;height:25px;border:1px solid var(--white);border-radius:50%;display:block}
</style>
</head>
<body>

<div class="abs announce">Handmade products by greatest artisans.</div>

<header class="abs nav">
  <div class="abs brand"><span class="brand-dot"></span>Lumora Lane</div>
  <nav class="abs menu">
    <span class="home">Home</span>
    <span class="dd">CRAFTS</span>
    <span class="dd">JEWELLERY</span>
    <span class="dd">ACCESSORIES</span>
    <span class="dd">APPARELS</span>
    <span class="dd">WALLDECOR</span>
  </nav>
  <div class="abs icons">
    <svg viewBox="0 0 16 16" aria-label="Search"><circle cx="7" cy="7" r="4" fill="none" stroke="#fff" stroke-width="1.4"/><line x1="10" y1="10" x2="13" y2="13" stroke="#fff" stroke-width="1.4"/></svg>
    <svg viewBox="0 0 16 16" aria-label="Cart"><path d="M1 3h2l2 7h8l2-5H4" fill="none" stroke="#fff" stroke-width="1.3"/><circle cx="6" cy="13" r="1.2" fill="#fff"/><circle cx="12" cy="13" r="1.2" fill="#fff"/><circle cx="14" cy="2.5" r="2.5" fill="#e53935"/></svg>
    <svg viewBox="0 0 16 16" aria-label="Wishlist"><path d="M8 14 2 8a3 3 0 0 1 6-4 3 3 0 0 1 6 4z" fill="none" stroke="#fff" stroke-width="1.3"/><circle cx="14" cy="2.5" r="2.5" fill="#e53935"/></svg>
    <svg viewBox="0 0 16 16" aria-label="Account"><circle cx="8" cy="5" r="3" fill="none" stroke="#fff" stroke-width="1.3"/><path d="M2 14c1-4 11-4 12 0" fill="none" stroke="#fff" stroke-width="1.3"/></svg>
  </div>
</header>

<section class="abs hero">
  <div class="abs hero-photo" role="img" aria-label="Carved wooden sunburst mirror on a wall above a shelf with small plants and a silver bowl"></div>
  <h1 class="abs hero-title">Wooden Wonder</h1>
  <p class="abs hero-sub">Hand Crafted Mirror</p>
  <div class="abs btn-dark">SHOP NOW</div>
  <svg class="abs arrow" style="left:137px;top:180px" viewBox="0 0 30 46"><polyline points="24,4 6,23 24,42" fill="none" stroke="#555" stroke-width="5"/></svg>
  <svg class="abs arrow" style="left:1013px;top:180px" viewBox="0 0 30 46"><polyline points="6,4 24,23 6,42" fill="none" stroke="#555" stroke-width="5"/></svg>
  <div class="abs dots"><i></i><i class="on"></i><i></i></div>
</section>

<h2 class="abs section-title" style="top:527px">Featured Products</h2>
<div class="abs rule" style="left:519px;top:554px;width:65px"></div>

<!-- product row 1 -->
<div class="abs card" style="left:235px;top:584px"><div class="card-photo ph-clay" role="img" aria-label="Hands carving a clay pot"><span class="badge">HOT</span></div><p class="card-name">Hand Crafted Clay Pot</p><p class="card-price">$90.00</p></div>
<div class="abs card" style="left:421px;top:584px"><div class="card-photo ph-beads" role="img" aria-label="Blue glass decor beads"><span class="badge">HOT</span></div><p class="card-name">Hand Crafted Decor Items</p><p class="card-price">$20.00</p></div>
<div class="abs card" style="left:607px;top:584px"><div class="card-photo ph-pipe" role="img" aria-label="Carved meerschaum pipe"><span class="badge">HOT</span></div><p class="card-name">Hand Crafted pipes</p><p class="card-price">$190.00</p></div>
<div class="abs card" style="left:792px;top:584px"><div class="card-photo ph-lantern" role="img" aria-label="Hanging mosaic lanterns"><span class="badge">HOT</span></div><p class="card-name">Hand Crafted Lanterns</p><p class="card-price">$70.00</p></div>

<!-- product row 2 -->
<div class="abs card" style="left:235px;top:850px"><div class="card-photo ph-clay" role="img" aria-label="Hands carving a clay pot"><span class="badge">HOT</span></div><p class="card-name">Hand Crafted Clay Pot</p><p class="card-price">$90.00</p></div>
<div class="abs card" style="left:421px;top:850px"><div class="card-photo ph-beads" role="img" aria-label="Blue glass decor beads"><span class="badge">HOT</span></div><p class="card-name">Hand Crafted Decor Items</p><p class="card-price">$20.00</p></div>
<div class="abs card" style="left:607px;top:850px"><div class="card-photo ph-pipe" role="img" aria-label="Carved meerschaum pipe"><span class="badge">HOT</span></div><p class="card-name">Hand Crafted pipes</p><p class="card-price">$190.00</p></div>
<div class="abs card" style="left:792px;top:850px"><div class="card-photo ph-lantern" role="img" aria-label="Hanging mosaic lanterns"><span class="badge">HOT</span></div><p class="card-name">Hand Crafted Lanterns</p><p class="card-price">$70.00</p></div>

<h2 class="abs section-title" style="top:1115px;font-size:19px">COLLECTIONS</h2>
<div class="abs rule" style="left:542px;top:1143px;width:76px"></div>

<!-- collections block 1 -->
<div class="abs tile big t-ceramic" style="left:232px;top:1181px;width:302px;height:364px" role="img" aria-label="Painted ceramic vase">CERAMIC<br>COLLECTIONS</div>
<div class="abs tile small t-embroid" style="left:543px;top:1181px;width:207px;height:196px" role="img" aria-label="Embroidered red carpets">EMBROID<br>COLLECTION</div>
<div class="abs tile small t-treasure" style="left:758px;top:1181px;width:207px;height:196px" role="img" aria-label="Brass teapots">Treasure<br>COLLECTION</div>
<div class="abs tile small t-unique" style="left:543px;top:1387px;width:207px;height:158px" role="img" aria-label="Decorated lidded jar">UNIQUE<br>COLLECTION</div>
<div class="abs tile small t-handy" style="left:758px;top:1387px;width:207px;height:158px" role="img" aria-label="Stacked woven textiles">HANDY<br>COllection</div>

<!-- collections block 2 -->
<div class="abs tile small t-embroid" style="left:231px;top:1557px;width:206px;height:196px" role="img" aria-label="Embroidered red carpets">EMBROID<br>COLLECTION</div>
<div class="abs tile small t-treasure" style="left:447px;top:1557px;width:206px;height:196px" role="img" aria-label="Brass teapots">Treasure<br>COLLECTION</div>
<div class="abs tile small t-unique" style="left:231px;top:1763px;width:206px;height:159px" role="img" aria-label="Decorated lidded jar">UNIQUE<br>COLLECTION</div>
<div class="abs tile small t-handy" style="left:447px;top:1763px;width:206px;height:159px" role="img" aria-label="Stacked woven textiles">HANDY<br>COllection</div>
<div class="abs tile big t-ceramic" style="left:665px;top:1557px;width:301px;height:365px" role="img" aria-label="Painted ceramic vase">CERAMIC<br>COLLECTIONS</div>

<!-- offers strip -->
<section class="abs strip"></section>
<p class="abs strip-head">Up to <span class="hl">30% Off</span> | On Decor and Embroiding Crafts <a>See all offers</a></p>
<div class="abs offer o1" style="left:257px;top:2012px" role="img" aria-label="Pierced brass table lamp"></div>
<div class="abs offer o2" style="left:399px;top:2012px" role="img" aria-label="Carved wooden standing mirror"></div>
<div class="abs offer o3" style="left:542px;top:2012px" role="img" aria-label="Framed artwork on a cream wall"></div>
<div class="abs offer o4" style="left:684px;top:2012px" role="img" aria-label="Metal lamp with black shade"></div>
<div class="abs offer o5" style="left:825px;top:2014px" role="img" aria-label="Hanging pierced pendant lamp"></div>
<svg class="abs arrow" style="left:136px;top:2077px" viewBox="0 0 30 46"><polyline points="24,4 6,23 24,42" fill="none" stroke="#555" stroke-width="5"/></svg>
<svg class="abs arrow" style="left:1014px;top:2077px" viewBox="0 0 30 46"><polyline points="6,4 24,23 6,42" fill="none" stroke="#555" stroke-width="5"/></svg>

<!-- promos -->
<div class="abs promo promo-lantern" style="left:243px;top:2264px" role="img" aria-label="Colourful mosaic lanterns">
  <p class="promo-text">30% OFFER ON HAND<br>CRAFTERD LANTERNS</p>
  <span class="btn-white">SHOP NOW</span>
</div>
<div class="abs promo promo-copper" style="left:616px;top:2264px" role="img" aria-label="Engraved copper bowls">
  <p class="promo-text">30% OFFER ON HAND<br>CRAFTERD LANTERNS</p>
  <span class="btn-white">SHOP NOW</span>
</div>

<!-- footer -->
<footer class="abs footer">
  <div class="abs f-col f-contact" style="left:303px;top:50px">
    <h4>Contact Info</h4>
    <p>Phone: +00 12345678</p>
    <p>Address: &nbsp;Lorem ipsum dolor sit amet</p>
    <p>Mail: info@lumoralane.com</p>
  </div>
  <div class="abs f-col" style="left:558px;top:50px">
    <h4>Information</h4>
    <p>About Us</p><p>Delivery Information</p><p>Privacy Policy</p><p>Terms &amp; Conditions</p><p>Brands</p>
  </div>
  <div class="abs f-col" style="left:698px;top:50px">
    <h4>General Info</h4>
    <p>FAQ's</p><p>Blog</p>
  </div>
  <div class="abs f-col" style="left:826px;top:50px">
    <h4>Help</h4>
    <p>Register</p><p>Login</p><p>Order History</p><p>Search</p>
  </div>
  <p class="abs follow">Follow Us</p>
  <div class="abs social" aria-label="Social links"><span></span><span></span><span></span><span></span></div>
</footer>
<div class="abs footer-base">Copyright © &nbsp;2021. All Rights Reserved.</div>

</body>
</html>
```